Re-Design WP Site BrightPebbles.info

Site Re-design. Also Need a Button for contact on main page. Need Great Looking products re designed. Also bonus if you can install a site SEO checker on the site.

BrightPebbles.info

```html
<!DOCTYPE html>
<html lang="en">
<head>
<meta charset="utf-8">
<title>BrightPebbles.info</title>
<link href="https://fonts.googleapis.com/css2?family=Montserrat+Alternates:wght@600;700;800&family=Poppins:wght@400;500;600;700&display=swap" rel="stylesheet">
<style>
:root{
  --blue:#0eaee0;
  --blue-bright:#19b7e6;
  --ink:#111318;
  --text:#5b5f66;
  --grey-bg:#ebebeb;
  --card-line:#6fd3f2;
  --red:#c90d0d;
  --black:#000;
  --white:#fff;
  --head:"Montserrat Alternates",sans-serif;
  --body:"Poppins",sans-serif;
}
*{box-sizing:border-box;margin:0;padding:0}
html,body{width:1200px;height:4605px;overflow:hidden}
body{font-family:var(--body);color:var(--ink);background:var(--white);position:relative}
section,footer{position:relative;width:1200px;overflow:hidden}
.abs{position:absolute}
.center-x{left:0;right:0;text-align:center}
.mark{width:22px;height:22px;border:2.5px solid var(--blue);border-radius:50%;margin:0 auto}
.mark.light{border-color:var(--white)}
.section-title{font-family:var(--head);font-weight:700;font-size:33px;color:var(--ink)}
.section-lead{font-size:15px;line-height:25px;color:var(--text);width:670px;margin:0 auto}
.btn{display:inline-flex;align-items:center;justify-content:center;border-radius:20px;font-weight:600;text-transform:uppercase;font-family:var(--body)}

/* hero */
.hero{height:644px;background:var(--white)}
.hero-photo{position:absolute;left:0;top:0;width:1200px;height:644px;background:
  linear-gradient(180deg,rgba(255,255,255,0) 78%,#fff 100%),
  radial-gradient(ellipse at 62% 55%,#2c7fb8 0%,#114a7e 30%,#0a2547 60%,#04101f 100%)}
.nav{position:absolute;top:38px;left:122px;width:956px;height:73px;background:var(--white);border-radius:12px}
.logo{position:absolute;display:flex;align-items:center;gap:8px;font-family:var(--head);font-weight:700;color:var(--blue);font-size:13px;letter-spacing:.5px}
.logo .dot{width:14px;height:14px;border-radius:50%;background:var(--blue)}
.nav .logo{left:38px;top:28px}
.menu{position:absolute;top:30px;left:0;font-size:12px;font-weight:600;text-transform:uppercase}
.menu a{position:absolute;color:var(--ink);text-decoration:none;white-space:nowrap}
.menu a.active{color:var(--blue)}
.nav .btn{position:absolute;top:19px;height:35px;font-size:11px;color:var(--white);background:linear-gradient(#26c1ef,#0c9ed3);box-shadow:0 2px 4px rgba(0,0,0,.25)}
.hero-title{top:252px;font-family:var(--head);font-weight:700;font-size:60px;color:var(--white)}
.hero-sub{top:338px;font-size:17.5px;line-height:24px;color:var(--white);width:720px;margin:0 auto}
.hero-cta{position:absolute;top:408px;left:526px;width:148px;height:34px;background:var(--blue-bright);color:var(--white);font-size:15px}
.dots{top:521px;display:flex;justify-content:center;gap:5px}
.dots span{width:7px;height:7px;border-radius:50%;background:#5fc7ee}
.dots span.on{background:var(--white)}

/* solutions */
.solutions{height:935px}
.cards{position:absolute;top:194px;left:123px;display:grid;grid-template-columns:313px 315px 314px;grid-auto-rows:328px;column-gap:7px;row-gap:7px}
.card{border:1.5px solid var(--card-line);text-align:center;position:relative}
.card.soft{border-color:#e3e3e3;box-shadow:0 0 6px rgba(0,0,0,.08)}
.card .ico{width:90px;height:90px;border-radius:50%;background:var(--blue);margin:38px auto 0;display:flex;align-items:center;justify-content:center}
.card h3{font-family:var(--head);font-weight:700;font-size:19px;margin-top:30px;letter-spacing:.3px}
.card p{font-size:13.5px;line-height:24px;color:var(--text);width:250px;margin:8px auto 0}
.more{display:inline-flex;align-items:center;gap:7px;color:var(--blue);font-size:13.5px;font-weight:600;margin-top:16px}
.more i{width:13px;height:13px;border-radius:50%;background:var(--blue);display:inline-flex;align-items:center;justify-content:center}

/* about */
.about{height:588px;background:linear-gradient(180deg,#10b2e3,#07a6da)}
.about-frame{position:absolute;left:175px;top:114px;width:401px;height:413px;border:2px solid #8fdcf5}
.about-photo{position:absolute;left:141px;top:91px;width:422px;height:424px;background:radial-gradient(circle at 50% 40%,#7fd1ff 0%,#1e6fc6 35%,#0c2f73 70%,#061a44 100%)}
.about-text{position:absolute;left:647px;top:102px;width:440px;color:var(--white)}
.about-text h2{font-family:var(--head);font-weight:700;font-size:33px;color:var(--white);margin-top:8px}
.about-text p{font-size:13.5px;line-height:22.5px;margin-top:10px}
.about-text .btn{margin-top:20px;width:97px;height:34px;background:var(--white);color:var(--blue);font-size:11px}

/* shop */
.shop{height:724px;background:var(--grey-bg)}
.products{position:absolute;top:218px;left:123px;display:flex;gap:11px}
.product{width:231px;height:381px;background:var(--blue-bright);position:relative;box-shadow:0 2px 6px rgba(0,0,0,.12)}
.product .pic{height:276px}
.pic.display{background:linear-gradient(180deg,#f7f7f7,#ececec)}
.pic.aerial{background:linear-gradient(135deg,#8f9590,#b3b6b2 50%,#858a86)}
.pic.leaf{background:linear-gradient(160deg,#6f9e35,#3f7320 50%,#24461a)}
.pic.leaf-mix{background:linear-gradient(135deg,#4d8526,#2f5a1a 60%,#5d7a49)}
.sale{position:absolute;top:0;left:0;background:var(--red);color:var(--white);font-weight:600;font-size:17px;padding:2px 14px 3px}
.product .info{text-align:center;color:var(--white);padding:14px 12px 0}
.product .name{font-size:11px;font-weight:600;line-height:17px}
.product .price{font-size:12px;font-weight:700;margin-top:3px}
.product .price s{font-weight:500}
.product .buy{font-size:11px;font-weight:700;color:var(--ink);margin-top:4px;display:inline-flex;align-items:center;gap:5px}
.product .buy i{width:9px;height:9px;border-radius:50%;background:var(--ink)}
.view-more{position:absolute;top:630px;left:527px;width:149px;height:35px;background:var(--blue-bright);color:var(--white);font-size:15px}

/* blogs */
.blogs{height:814px}
.blog-grid{position:absolute;top:209px;left:123px;width:956px;display:grid;grid-template-columns:repeat(3,1fr);grid-auto-rows:264px}
.b-photo.laptop{background:linear-gradient(135deg,#052c4a,#0b83b5 55%,#56d3f2)}
.b-photo.city{background:linear-gradient(180deg,#0b1b3d,#1a4d9a 50%,#0b2350)}
.b-photo.hands{background:radial-gradient(circle at 50% 40%,#c9eaff,#4c8ccf 35%,#13244a 75%)}
.b-text{padding:44px 24px 0;background:var(--white)}
.tag{display:inline-block;background:#545454;color:var(--white);font-size:11px;padding:4px 13px;border-radius:12px}
.b-text h4{font-size:11.5px;font-weight:700;text-transform:uppercase;margin-top:12px;letter-spacing:.2px}
.b-text p{font-size:11.5px;line-height:20px;color:var(--text);margin-top:5px}
.b-text .more{font-size:11px;margin-top:4px}
.b-text .more i{width:10px;height:10px}

/* contact */
.contact{height:585px;background:linear-gradient(180deg,#0aa7dc,#0ba9de)}
.contact h2{color:var(--white)}
.form{position:absolute;top:152px;left:154px;width:892px;display:grid;grid-template-columns:436px 436px;gap:17px 20px}
.field{height:52px;background:var(--white);border-radius:4px;font-size:12.5px;color:#888;padding:17px 28px}
.field.message{grid-column:1 / 3;height:129px}
.submit{position:absolute;top:447px;left:535px;width:148px;height:36px;background:var(--white);color:var(--blue);font-size:15px}

/* footer */
.site-footer{height:315px;background:var(--black);color:var(--white)}
.site-footer h5{font-family:var(--head);font-weight:700;font-size:18px;text-transform:uppercase;position:absolute;top:82px}
.foot-logo{left:125px;top:160px;color:var(--white);font-size:15px}
.foot-logo .dot{background:var(--white)}
.links{position:absolute;left:409px;top:118px;list-style:none;font-size:13px;line-height:24px}
.contact-list{position:absolute;left:628px;top:112px;list-style:none;font-size:11px}
.contact-list li{display:flex;align-items:center;gap:14px;margin-bottom:12px;line-height:17px}
.contact-list .c-ico{width:28px;height:28px;border-radius:50%;background:var(--blue);flex:none;display:flex;align-items:center;justify-content:center}
.social{position:absolute;left:905px;top:118px;list-style:none;font-size:11.5px}
.social li{display:flex;align-items:center;gap:10px;height:29px}
.social i{width:20px;height:20px;border-radius:50%;background:var(--blue)}
.rule{position:absolute;left:122px;top:255px;width:956px;height:1px;background:#555}
.copy{top:279px;font-size:11px;color:#ddd}
</style>
</head>
<body>

<section class="hero">
  <div class="hero-photo" role="img" aria-label="Photo of hands typing on a laptop beneath a glowing blue digital globe and network"></div>
  <nav class="nav">
    <div class="logo"><span class="dot"></span>BRIGHTPEBBLES.info</div>
    <div class="menu">
      <a class="active" style="left:259px">Home</a>
      <a style="left:333px">Shop</a>
      <a style="left:405px">Solutions</a>
      <a style="left:516px">Blog</a>
      <a style="left:587px">Contact Us</a>
    </div>
    <a class="btn" style="left:704px;width:98px">Login</a>
    <a class="btn" style="left:820px;width:95px">Sign Up</a>
  </nav>
  <h1 class="abs center-x hero-title">Bright Pebbles</h1>
  <p class="abs center-x hero-sub">We’re a studio of creators inventing unique and effective IT applications providing solutions that solve real world problems.</p>
  <a class="btn hero-cta">Contact Us</a>
  <div class="abs center-x dots"><span></span><span></span><span></span><span class="on"></span><span></span></div>
</section>

<section class="solutions">
  <div class="abs center-x" style="top:43px"><div class="mark"></div></div>
  <h2 class="abs center-x section-title" style="top:66px">Our Solutions</h2>
  <p class="abs center-x section-lead" style="top:114px">It is a long established fact that a reader will be distracted by the readable content of a page when looking at its layout.</p>
  <div class="cards">
    <div class="card">
      <div class="ico"><svg width="46" height="46" viewBox="0 0 46 46" fill="none" stroke="#fff" stroke-width="2"><rect x="4" y="6" width="16" height="14" rx="2"/><rect x="26" y="6" width="16" height="10" rx="2"/><rect x="4" y="26" width="16" height="14" rx="2"/><path d="M26 40 L42 24 M26 24 h16 v16"/></svg></div>
      <h3>ADVERTISING</h3>
      <p>The standard chunk of Lorem Ipsum used since the 1500s is reproduced below for those interested.</p>
      <span class="more">LEARN MORE <i><svg width="7" height="7" viewBox="0 0 7 7"><path d="M2 1 L5 3.5 L2 6" stroke="#fff" fill="none" stroke-width="1.4"/></svg></i></span>
    </div>
    <div class="card soft">
      <div class="ico"><svg width="46" height="46" viewBox="0 0 46 46" fill="none" stroke="#fff" stroke-width="2"><rect x="4" y="4" width="38" height="26" rx="3"/><rect x="12" y="30" width="5" height="12"/><rect x="21" y="24" width="5" height="18"/><rect x="30" y="18" width="5" height="24"/><path d="M10 14 h4 M18 14 h4 M26 14 h4"/></svg></div>
      <h3>REPUTATION</h3>
      <p>The standard chunk of Lorem Ipsum used since the 1500s is reproduced below for those interested.</p>
      <span class="more">LEARN MORE <i><svg width="7" height="7" viewBox="0 0 7 7"><path d="M2 1 L5 3.5 L2 6" stroke="#fff" fill="none" stroke-width="1.4"/></svg></i></span>
    </div>
    <div class="card">
      <div class="ico"><svg width="46" height="46" viewBox="0 0 46 46" fill="none" stroke="#fff" stroke-width="2"><rect x="9" y="6" width="28" height="36" rx="3"/><path d="M15 15 l2 2 4-4 M24 15 h8 M15 24 l2 2 4-4 M24 24 h8 M15 33 l2 2 4-4 M24 33 h8"/></svg></div>
      <h3>LISTINGS</h3>
      <p>The standard chunk of Lorem Ipsum used since the 1500s is reproduced below for those interested.</p>
      <span class="more">LEARN MORE <i><svg width="7" height="7" viewBox="0 0 7 7"><path d="M2 1 L5 3.5 L2 6" stroke="#fff" fill="none" stroke-width="1.4"/></svg></i></span>
    </div>
    <div class="card">
      <div class="ico"><svg width="46" height="46" viewBox="0 0 46 46" fill="none" stroke="#fff" stroke-width="2"><rect x="4" y="6" width="38" height="28" rx="2"/><path d="M4 12 h38 M16 40 h14 M23 34 v6 M10 18 h12 v10 h-12z M26 18 h10 M26 23 h10 M26 28 h8"/></svg></div>
      <h3>WEBSITE</h3>
      <p>The standard chunk of Lorem Ipsum used since the 1500s is reproduced below for those interested.</p>
      <span class="more">LEARN MORE <i><svg width="7" height="7" viewBox="0 0 7 7"><path d="M2 1 L5 3.5 L2 6" stroke="#fff" fill="none" stroke-width="1.4"/></svg></i></span>
    </div>
    <div class="card">
      <div class="ico"><svg width="46" height="46" viewBox="0 0 46 46" fill="none" stroke="#fff" stroke-width="2"><rect x="4" y="12" width="20" height="18" rx="3"/><rect x="22" y="4" width="20" height="16" rx="3"/><circle cx="30" cy="34" r="8"/><path d="M10 19 h8 M10 23 h8 M28 12 h8"/></svg></div>
      <h3>SOCIAL</h3>
      <p>The standard chunk of Lorem Ipsum used since the 1500s is reproduced below for those interested.</p>
      <span class="more">LEARN MORE <i><svg width="7" height="7" viewBox="0 0 7 7"><path d="M2 1 L5 3.5 L2 6" stroke="#fff" fill="none" stroke-width="1.4"/></svg></i></span>
    </div>
    <div class="card">
      <div class="ico"><svg width="46" height="46" viewBox="0 0 46 46" fill="none" stroke="#fff" stroke-width="2"><circle cx="23" cy="23" r="17"/><circle cx="23" cy="19" r="5"/><path d="M14 34 c2-6 16-6 18 0 M6 23 h4 M36 23 h4"/></svg></div>
      <h3>CONTENT &amp; EXPERIENCE</h3>
      <p>The standard chunk of Lorem Ipsum used since the 1500s is reproduced below for those interested.</p>
      <span class="more">LEARN MORE <i><svg width="7" height="7" viewBox="0 0 7 7"><path d="M2 1 L5 3.5 L2 6" stroke="#fff" fill="none" stroke-width="1.4"/></svg></i></span>
    </div>
  </div>
</section>

<section class="about">
  <div class="about-frame"></div>
  <div class="about-photo" role="img" aria-label="Photo of an open hand holding a glowing cloud symbol above a digital globe"></div>
  <div class="about-text">
    <div class="mark light" style="margin:0"></div>
    <h2>About Us</h2>
    <p>Contrary to popular belief, Lorem Ipsum is not simply random text. It has roots in a piece of classical Latin literature from 45 BC, making it over 2000 years old. Rowan Mercer, a Latin professor at Hollybrook College in Virginia, looked up one of the more obscure Latin words, consectetur, from a Lorem Ipsum passage, and going through the cites of the word in classical literature,</p>
    <p style="margin-top:22px">This book is a treatise on the theory of ethics, very popular during the Renaissance. The first line of Lorem Ipsum, "Lorem ipsum dolor sit amet..",<br>section 1.10.32.</p>
    <a class="btn">Read More</a>
  </div>
</section>

<section class="shop">
  <div class="abs center-x" style="top:57px"><div class="mark"></div></div>
  <h2 class="abs center-x section-title" style="top:80px">Shop Our Products</h2>
  <p class="abs center-x section-lead" style="top:128px">It is a long established fact that a reader will be distracted by the readable content of a page when looking at its layout.</p>
  <div class="products">
    <div class="product">
      <div class="pic display" role="img" aria-label="Product photo of a digital giveaway display stand"></div>
      <div class="info">
        <div class="name">Social Media Marketing! &amp; Local<br>Local Map Biz Boost</div>
        <div class="price"><s>$6,995.00</s> $3,495.00 / month</div>
        <div class="buy">SHOP NOW <i></i></div>
      </div>
    </div>
    <div class="product">
      <div class="pic aerial" role="img" aria-label="Aerial map photo with a highlighted geo fence zone"></div>
      <span class="sale">Sale</span>
      <div class="info">
        <div class="name">Digital Marketing – GEO Fence –<br>Track Number</div>
        <div class="price"><s>$1,295.00</s> $895.00 / month</div>
        <div class="buy">SHOP NOW <i></i></div>
      </div>
    </div>
    <div class="product">
      <div class="pic leaf" role="img" aria-label="Photo of green leafy plants"></div>
      <div class="info">
        <div class="name">Cannabis Targeted Display &amp;<br>GEO Fencing</div>
        <div class="price"><s>$6,495.00</s> $4,997.00 / month</div>
        <div class="buy">SHOP NOW <i></i></div>
      </div>
    </div>
    <div class="product">
      <div class="pic leaf-mix" role="img" aria-label="Photo of green plants beside a giveaway display stand"></div>
      <div class="info">
        <div class="name">#1 Cannabis Advertising w/GEO<br>Fence! Social Media Marketing!</div>
        <div class="price"><s>$18,995.00</s> $8,495.00 / month</div>
        <div class="buy">SHOP NOW <i></i></div>
      </div>
    </div>
  </div>
  <a class="btn view-more">View More</a>
</section>

<section class="blogs">
  <div class="abs center-x" style="top:50px"><div class="mark"></div></div>
  <h2 class="abs center-x section-title" style="top:76px">Latest Blogs</h2>
  <p class="abs center-x section-lead" style="top:125px">It is a long established fact that a reader will be distracted by the readable content of a page when looking at its layout.</p>
  <div class="blog-grid">
    <div class="b-photo laptop" role="img" aria-label="Photo of hands typing on a laptop with a glowing cloud above"></div>
    <div class="b-text">
      <span class="tag">Trovana</span>
      <h4>Cost of Search SEO Report</h4>
      <p>Give you an idea of what to expect. Uh, chose Maple Falls Oregon, a city I live near., 76,000 population. I searched chiropractor. And I actually pulled out the best keywords. For local search.</p>
      <span class="more">LEARN MORE <i></i></span>
    </div>
    <div class="b-photo city" role="img" aria-label="Illustration of a cloud with upload and download arrows over a night city"></div>
    <div class="b-text">
      <span class="tag">Trovana</span>
      <h4>Cost of Search SEO Report</h4>
      <p>Give you an idea of what to expect. Uh, chose Maple Falls Oregon, a city I live near., 76,000 population. I searched chiropractor. And I actually pulled out the best keywords. For local search.</p>
      <span class="more">LEARN MORE <i></i></span>
    </div>
    <div class="b-photo hands" role="img" aria-label="Photo of two hands cupping a glowing cloud inside a network sphere"></div>
    <div class="b-text">
      <span class="tag">Trovana</span>
      <h4>Cost of Search SEO Report</h4>
      <p>Give you an idea of what to expect. Uh, chose Maple Falls Oregon, a city I live near., 76,000 population. I searched chiropractor. And I actually pulled out the best keywords. For local search.</p>
      <span class="more">LEARN MORE <i></i></span>
    </div>
  </div>
</section>

<section class="contact">
  <div class="abs center-x" style="top:46px"><div class="mark light"></div></div>
  <h2 class="abs center-x section-title" style="top:74px">Contact Us</h2>
  <div class="form">
    <div class="field">First Name</div>
    <div class="field">Last Name</div>
    <div class="field">Email Address</div>
    <div class="field">Phone Number</div>
    <div class="field message">Leave Your Message.....</div>
  </div>
  <a class="btn submit">Submit Now</a>
</section>

<footer class="site-footer">
  <div class="logo foot-logo"><span class="dot"></span>BRIGHTPEBBLES.info</div>
  <h5 style="left:409px">Quick Links</h5>
  <ul class="links"><li>Home</li><li>About Us</li><li>Solutions</li><li>Shop</li><li>Contact Us</li></ul>
  <h5 style="left:624px">Contact Us</h5>
  <ul class="contact-list">
    <li><span class="c-ico"><svg width="12" height="16" viewBox="0 0 12 16"><path d="M6 0 C2.7 0 0 2.6 0 5.8 C0 10 6 16 6 16 S12 10 12 5.8 C12 2.6 9.3 0 6 0Z" fill="#fff"/><circle cx="6" cy="6" r="2.2" fill="#0eaee0"/></svg></span>The standard chunk of Lorem<br>Ipsum used since 1500</li>
    <li><span class="c-ico"><svg width="14" height="14" viewBox="0 0 24 24"><path d="M6.6 10.8c1.4 2.8 3.8 5.1 6.6 6.6l2.2-2.2c.3-.3.7-.4 1-.2 1.1.4 2.3.6 3.6.6.6 0 1 .4 1 1V20c0 .6-.4 1-1 1C10.6 21 3 13.4 3 4c0-.6.4-1 1-1h3.5c.6 0 1 .4 1 1 0 1.3.2 2.5.6 3.6.1.3 0 .7-.2 1l-2.3 2.2z" fill="#fff"/></svg></span>+1 444 444 4444</li>
    <li><span class="c-ico"><svg width="14" height="11" viewBox="0 0 14 11"><rect x="0.7" y="0.7" width="12.6" height="9.6" rx="1" fill="none" stroke="#fff" stroke-width="1.4"/><path d="M1 1.5 L7 6 L13 1.5" fill="none" stroke="#fff" stroke-width="1.4"/></svg></span>info@brightpebbles.info</li>
  </ul>
  <h5 style="left:905px">Stay In Touch</h5>
  <ul class="social">
    <li><i></i>Friendwall</li>
    <li><i></i>Snapgrid</li>
    <li><i></i>Workline</li>
    <li><i></i>Chirper</li>
  </ul>
  <div class="rule"></div>
  <p class="abs center-x copy">Copyright 2022 © Bright Pebbles | All Rights Reserved.</p>
</footer>

</body>
</html>
```